Modernise Business Card

Our company has been operating for 10 years. With the start of the new decade we are looking to refresh our business card design. We manufacture a range of industrial product shipping to customers internationally. A copy of our current card, both sides, is attached. We are looking for a mature professional appearance.

```html
<!DOCTYPE html>
<html lang="en">
<head>
<meta charset="UTF-8">
<title>Vantrel Business Card</title>
<link href="https://fonts.googleapis.com/css2?family=Poppins:wght@400;500;700;800&family=Archivo+Black&display=swap" rel="stylesheet">
<style>
  :root {
    --bg: #8e8e8e;
    --brown: #51473a;
    --blue: #09acd6;
    --white: #ffffff;
  }
  * { margin: 0; padding: 0; box-sizing: border-box; }
  html, body { width: 1200px; height: 960px; overflow: hidden; }
  body {
    background: var(--bg);
    font-family: "Poppins", sans-serif;
    display: flex;
    flex-direction: column;
    align-items: center;
    justify-content: center;
    gap: 56px;
  }
  .card {
    width: 640px;
    height: 366px;
    position: relative;
    overflow: hidden;
    box-shadow: 0 10px 24px rgba(0,0,0,0.3);
  }
  /* Front */
  .card-front {
    background: var(--brown);
    border-bottom: 4px solid var(--blue);
    display: flex;
    flex-direction: column;
    align-items: center;
    justify-content: center;
    gap: 10px;
  }
  .brand-name {
    font-family: "Poppins", sans-serif;
    font-weight: 800;
    color: var(--blue);
    font-size: 76px;
    line-height: 1;
    letter-spacing: -1px;
  }
  .tagline {
    color: var(--white);
    font-size: 15px;
    font-weight: 500;
  }
  /* Back */
  .card-back { background: var(--white); }
  .back-brand {
    position: absolute;
    top: 44px;
    left: 0; right: 0;
    text-align: center;
    font-size: 72px;
  }
  .name-rule {
    position: absolute;
    top: 156px;
    left: 0; right: 0;
    display: flex;
    align-items: center;
    gap: 14px;
  }
  .name-rule .line { flex: 1; height: 6px; background: var(--brown); }
  .person-name {
    font-family: "Archivo Black", sans-serif;
    color: var(--blue);
    font-size: 30px;
    letter-spacing: 0.5px;
  }
  .contact-band {
    position: absolute;
    left: 0; right: 0; bottom: 0;
    height: 156px;
    background: var(--blue);
    border-top: 10px solid var(--brown);
    display: flex;
    justify-content: center;
    align-items: center;
    color: var(--white);
    font-size: 16px;
    font-weight: 500;
    line-height: 1.35;
  }
  .gap-strip {
    position: absolute;
    left: 0; right: 0;
    bottom: 166px;
    height: 20px;
    background: var(--white);
  }
  .address { text-align: right; padding-right: 22px; }
  .divider { width: 2px; height: 96px; background: var(--white); }
  .contacts { padding-left: 22px; }
</style>
</head>
<body>
  <section class="card card-front">
    <div class="brand-name">Vantrel</div>
    <p class="tagline">Hydraulic Adapters • Hose Fittings • Quick Couplings</p>
  </section>

  <section class="card card-back">
    <div class="brand-name back-brand">Vantrel</div>
    <div class="name-rule">
      <span class="line"></span>
      <span class="person-name">REID HALSTON</span>
      <span class="line"></span>
    </div>
    <div class="contact-band">
      <div class="address">
        1208-3, Lumen Tower<br>
        77 Harbour View Road<br>
        Eastgate District<br>
        Ningbo 315000 China
      </div>
      <span class="divider"></span>
      <div class="contacts">
        China : +86 138 5520 7714<br>
        Australia: +61 412 877 309<br>
        rhalston@vantrelfittings.com<br>
        www.vantrelfittings.com
      </div>
    </div>
  </section>
</body>
</html>
```